Radiology Department needs a series of 3 facebook posts - similar design

We need a series of 3 posts for our facebook page, each one presenting the activity of one of 3 physicians.
The main design elements can be the same, the only thing that will change between posts will be the field of activity and name of the physician and the representative image of its activity.
If needed the design elements can be slightly different between posts for better adjustment to the representative images.
You can find as an attachment:
- Manual of institutional identity of the Hospital (Velmor Clinica)
- Our facebook cover page
- Our department video
- The representative images for each post, identified with the name of each physician
- The Institutional identity manual with the logo of "Brisa Medical School" - just for Dr Tomas Brandilo post.
So, each one of the three posts should state the name and field of activity of each physician, including somehow the corresponding representative image, and should have background innovative design elements.
Post 1:
Name of the physician: Prof. Doutor Rui Castelvo
Field of activity: Imagiologia Reumatológica e do Sistema Músculo-Esquelético
Image as an attachment
Post 2:
Name of the physician: Prof.ª Doutora Inês Barroca
Field of activity: Imagiologia Cardíaca
Image as an attachment
Post 3:
Name of the physician: Dr. Tomas Lupo
Field of activity: Tese de Doutoramento em Curso - Identificação da Lesão Cartilagínea Precoce. Com orientação do Prof. Doutor Rui Castelvo e Prof.ª Doutora Inês Sofia Carvalhal.
Image as an attachment
Just for Dr Tomas Lupo, the logo of Brisa Medical School should also be included (please check the corresponding institutional identity manual that was just added in documents).
Updates

Just for Dr Tomas Brandilo, the logo of Brisa Medical School should also be included (please check the corresponding institutional identity manual that was just added in documents).

Please note that we are just looking for 3 facebook POSTS, not facebook cover page, thanks.

Please kindly note that we are looking for facebook POST and NOT facebook cover page.

Target Market(s)

General Population

Industry/Entity Type

Health

Font styles to use
Other font styles liked:
• Check manual of institutional identity and try to approach if appropriate

Requirements
Must have
• Check project description.
Nice to have
• If the designer finds appropriate, the logo of the Hospital would be nice in all the three posts, the most simple one just stating "VelmorClinica" - please check the attached manual of institutional identity

```html
<!DOCTYPE html>
<html lang="pt">
<head>
<meta charset="utf-8">
<title>VelmorClinica — Dr. Tomas Lupo</title>
<link rel="stylesheet" href="https://fonts.googleapis.com/css2?family=Arimo:wght@400;700&display=swap">
<style>
  :root {
    --page: #ffffff;
    --teal: #0a5565;
    --teal-light: #0e6577;
    --yellow: #fbb522;
    --white: #ffffff;
    --ink: #2a2a2a;
    --photo-dark: #2f2a24;
    --photo-mid: #7d7469;
    --scan-deep: #0b1a7a;
    --scan-bright: #2a49e0;
    --connector: #b9b9b9;
  }
  * { margin: 0; padding: 0; box-sizing: border-box; }
  html, body {
    width: 1200px; height: 901px; overflow: hidden;
    background: var(--page);
    font-family: "Arimo", Arial, sans-serif;
  }
  .post {
    position: absolute; left: 30px; top: 152px;
    width: 1139px; height: 597px;
    overflow: hidden;
    background: var(--teal);
  }
  .post__shapes { position: absolute; inset: 0; }
  .brand {
    position: absolute; left: 47px; top: 50px;
    display: flex; align-items: center; gap: 8px;
    color: var(--white); font-weight: 700; font-size: 27px;
  }
  .brand__dot {
    width: 44px; height: 44px; border-radius: 50%;
    background: var(--white);
  }
  .thesis {
    position: absolute; left: 45px; top: 155px; width: 420px;
    color: var(--white); font-weight: 700; font-size: 14.5px; line-height: 20px;
  }
  .bar { position: absolute; background: var(--white); }
  .bar--one { left: 73px; top: 374px; width: 348px; height: 8px; }
  .bar--two { left: 45px; top: 393px; width: 349px; height: 15px; }
  .bar--three { left: 428px; top: 514px; width: 173px; height: 10px; }
  .physician {
    position: absolute; left: 75px; top: 438px; width: 400px;
    text-align: center;
    color: var(--white); font-weight: 700; font-size: 40px;
  }
  .school {
    position: absolute; left: 173px; top: 499px;
    width: 208px; height: 39px;
    background: var(--white);
    display: flex; align-items: center; justify-content: center;
    color: var(--ink); font-weight: 700; font-size: 15px; letter-spacing: 0.5px;
  }
</style>
</head>
<body>
  <main class="post">
    <svg class="post__shapes" width="1139" height="597" viewBox="0 0 1139 597">
      <defs>
        <linearGradient id="photo-tone" x1="0" y1="0" x2="1" y2="1">
          <stop offset="0" stop-color="var(--photo-dark)"/>
          <stop offset="0.5" stop-color="var(--photo-mid)"/>
          <stop offset="1" stop-color="var(--photo-dark)"/>
        </linearGradient>
        <radialGradient id="scan-tone" cx="0.5" cy="0.45" r="0.6">
          <stop offset="0" stop-color="var(--scan-bright)"/>
          <stop offset="1" stop-color="var(--scan-deep)"/>
        </radialGradient>
      </defs>
      <!-- background stripes -->
      <polygon points="320,0 470,0 360,597 210,597" fill="var(--teal-light)" opacity="0.55"/>
      <polygon points="530,0 620,0 510,597 420,597" fill="var(--teal-light)" opacity="0.45"/>
      <polygon points="970,0 1139,0 1139,597 860,597" fill="var(--teal-light)" opacity="0.5"/>
      <!-- yellow panel -->
      <path d="M158,307 Q148,307 145,320 L66,597 L839,597 L916,307 Z" fill="var(--yellow)"/>
      <!-- reading room photo -->
      <g role="img" aria-label="Radiology reading room with image monitors, softly blurred">
        <path d="M705,74 L1139,74 L1139,568 L610,568 Q592,568 596,550 L690,88 Q694,74 705,74 Z" fill="url(#photo-tone)"/>
      </g>
      <!-- connector -->
      <polyline points="733,229 846,229 933,351" fill="none" stroke="var(--connector)" stroke-width="2"/>
      <circle cx="933" cy="351" r="7" fill="var(--connector)"/>
      <!-- scan medallion -->
      <circle cx="602" cy="244" r="158" fill="var(--white)" opacity="0.12"/>
      <circle cx="602" cy="244" r="150" fill="none" stroke="var(--white)" stroke-width="3" opacity="0.3"/>
      <circle cx="602" cy="244" r="141" fill="var(--white)" opacity="0.75"/>
      <g role="img" aria-label="Colour-mapped axial MRI of the knee cartilage">
        <circle cx="602" cy="244" r="130" fill="url(#scan-tone)"/>
      </g>
    </svg>

    <div class="brand"><span class="brand__dot"></span>VelmorClinica</div>

    <p class="thesis">Tese de Doutoramento em Curso -<br>Identificação da Lesão Cartilagínea Precoce.<br>Com orientação do Prof. Doutor Rui Castelvo e<br>Prof.ª Doutora Inês Sofia Carvalhal</p>

    <span class="bar bar--one"></span>
    <span class="bar bar--two"></span>
    <span class="bar bar--three"></span>

    <h1 class="physician">Dr. Tomas Lupo</h1>
    <div class="school">BRISA MEDICAL SCHOOL</div>
  </main>
</body>
</html>
```